Redesign responsive website and logo for webshop platform

Redesign our applications old website with a new clean, crisp modern looking style that is responsive.

Our application is a cloud based, free ecommerce platform that lets users set up their own webshops within minutes. (Similar to Mabrook https://mabrook.example/l/sell)

Our old website: http://sv.vendlyx.example/

I need redesigned HTML + CSS for the following three pages:
* Landing Page:
(Old page: http://sv.vendlyx.example/)
I have attached a mockup of a proposed layout/structure for the landing page.
- Pricing comparision/features page
(Old page http://sv.vendlyx.example/t/funktioner)
- Generic "article" page:
(Old page http://sv.vendlyx.example/d/redigerasida)

The pages must responsive using HTML 5/CSS 3 (I prefer Bootstrap 3 if possible).

I also need a redesign of the logotype.

If you have any questions don't hesitate to ask and we will provide whatever is needed to you.

Logo Text

Vendlyx

Coding

Coded - Design and coding required

Number of Pages Required

3 page

Font styles to use
Serif
Sans Serif

```html
<!DOCTYPE html>
<html lang="sv">
<head>
<meta charset="utf-8">
<title>Vendlyx – Starta en gratis webshop</title>
<link rel="stylesheet" href="https://fonts.googleapis.com/css2?family=Montserrat:wght@400;600;700&family=Open+Sans:wght@400;600;700&display=swap">
<style>
:root{
  --blue:#0b8dd0;
  --blue-dark:#1d5aa9;
  --btn:#1f62b5;
  --light:#e9f3f9;
  --ink:#555b60;
  --white:#ffffff;
  --hero-a:#26435a;
  --hero-b:#3b6880;
  --panel:rgba(22,32,40,.82);
}
*{margin:0;padding:0;box-sizing:border-box}
html,body{width:1051px;height:1200px;overflow:hidden;background:var(--white)}
body{position:relative;font-family:"Open Sans",Arial,sans-serif;color:var(--ink)}
.abs{position:absolute}

/* hero */
.hero{left:0;top:0;width:1051px;height:528px;overflow:hidden}
.hero-photo{position:absolute;inset:0;background:radial-gradient(ellipse at 25% 45%,#7a8d99 0%,var(--hero-b) 35%,var(--hero-a) 75%,#1d3447 100%)}
.brand{left:174px;top:18px;font-family:"Montserrat",sans-serif;font-weight:700;font-size:29px;color:var(--white);letter-spacing:.5px}
.top-links{left:682px;top:17px;display:flex;gap:14px;font-family:"Montserrat",sans-serif;font-size:9px;font-weight:600;color:var(--white);align-items:center}
.top-links span{display:flex;align-items:center;gap:5px}
.dot-mark{width:7px;height:7px;border-radius:50%;background:var(--white);display:inline-block}
.hero-title{left:174px;top:126px;font-family:"Montserrat",sans-serif;font-weight:700;font-size:48px;line-height:58px;color:var(--white)}
.hero-text{left:175px;top:252px;width:398px;font-size:16px;line-height:24px;color:var(--white);text-align:justify}
.hero-btn{left:176px;top:358px;width:143px;height:31px;background:linear-gradient(#1a8ad4,#1563b0);color:var(--white);font-family:"Montserrat",sans-serif;font-size:13px;line-height:31px;text-align:center;border-radius:2px}
.register{left:606px;top:165px;width:270px;height:203px;background:var(--panel)}
.register h2{position:absolute;top:18px;width:100%;text-align:center;font-family:"Montserrat",sans-serif;font-weight:700;font-size:17px;color:var(--white)}
.field{position:absolute;left:25px;width:222px;height:26px;background:var(--white);font-family:"Montserrat",sans-serif;font-size:8px;font-weight:600;color:#222;padding-left:14px;line-height:26px}
.reg-btn{position:absolute;left:25px;top:149px;width:222px;height:26px;background:var(--btn);color:var(--white);font-family:"Montserrat",sans-serif;font-weight:600;font-size:11px;text-align:center;line-height:26px}
.slide-dots{left:467px;top:470px;display:flex;gap:6px}
.slide-dots i{display:block;width:35px;height:2px;background:var(--white)}
.slide-dots i.on{background:var(--blue)}

/* features */
.feature{width:340px}
.feature .icon{position:absolute;left:0;top:0;width:42px;height:44px;background:var(--blue);display:flex;align-items:center;justify-content:center}
.feature h3{position:absolute;left:51px;top:-4px;font-family:"Montserrat",sans-serif;font-weight:400;font-size:18px;color:var(--blue);white-space:nowrap}
.feature p{position:absolute;left:54px;top:28px;width:265px;font-size:9.6px;line-height:16px;color:var(--ink)}
.rule{left:0;top:872px;width:1051px;height:1px;background:#c9cdd0}

/* small feature cards */
.card{width:239px;height:92px;display:flex}
.card .num{width:75px;background:var(--light);font-family:"Montserrat",sans-serif;font-size:30px;color:var(--blue);display:flex;align-items:center;justify-content:center}
.card .body{flex:1;background:var(--blue);color:var(--white);padding:12px 13px}
.card small{display:block;font-family:"Montserrat",sans-serif;font-size:10px;line-height:12px}
.card strong{display:block;font-family:"Montserrat",sans-serif;font-weight:400;font-size:17px;line-height:20px;margin-bottom:3px}
.card p{font-size:9.6px;line-height:16px}

/* footer */
.foot-left{left:0;top:1162px;width:277px;height:38px;background:var(--light);display:flex;gap:18px;align-items:center;justify-content:center;padding-left:34px}
.foot-left i{width:8px;height:8px;background:var(--blue-dark);border-radius:50%;display:block}
.foot-right{left:277px;top:1162px;width:774px;height:38px;background:var(--blue-dark);color:var(--white);font-size:8px;line-height:38px;text-align:right;padding-right:145px}
</style>
</head>
<body>

<header class="abs hero">
  <div class="hero-photo" role="img" aria-label="Hand holding a tablet with a glowing network of connected points"></div>
  <div class="abs brand">Vendlyx</div>
  <nav class="abs top-links">
    <span><svg width="9" height="7" viewBox="0 0 9 7"><rect x=".5" y=".5" width="8" height="6" fill="none" stroke="#fff"/><path d="M.5 .5l4 3 4-3" fill="none" stroke="#fff"/></svg>info@vendlyx.example</span>
    <span><i class="dot-mark"></i>Vendlyx på Chirply</span>
  </nav>
  <h1 class="abs hero-title">Starta en gratis<br>webshop</h1>
  <p class="abs hero-text">Vendlyx är en tjänst som låter dig starta en komplett internetbutik. Tjänsten är gratis och har allt som krävs för att du ska komma igång med din verksamhet och sälja produkter online.</p>
  <div class="abs hero-btn">Skapa en webshop</div>
  <form class="abs register">
    <h2>REGISTRATION</h2>
    <div class="field" style="top:53px">Enter your email id</div>
    <div class="field" style="top:85px">Password</div>
    <div class="field" style="top:117px">Re Enter Password</div>
    <div class="reg-btn">REGISTER</div>
  </form>
  <div class="abs slide-dots"><i class="on"></i><i></i><i></i></div>
</header>

<section>
  <div class="abs feature" style="left:174px;top:570px">
    <div class="icon"><svg width="18" height="18" viewBox="0 0 18 18" fill="none" stroke="#fff" stroke-width="1.5"><rect x="2" y="8" width="3" height="8"/><path d="M5 9l4-6c1.5 0 2 1 1.5 2.5L10 8h5c1 0 1.5 1 1 2l-2 5c-.3.7-1 1-1.7 1H5"/></svg></div>
    <h3>Kom igång på 5 minuter</h3>
    <p>Att starta en ebutik med Vendlyx tar inte mer än 5 minuter. Skapa ett konto för att komma igång. Ingenting behöver installeras på din dator.</p>
  </div>
  <div class="abs feature" style="left:564px;top:570px">
    <div class="icon"><svg width="18" height="18" viewBox="0 0 18 18" fill="#fff"><path d="M1 3h3l2 8h9l2-6H5.5" fill="none" stroke="#fff" stroke-width="1.6"/><circle cx="7" cy="14.5" r="1.5"/><circle cx="14" cy="14.5" r="1.5"/></svg></div>
    <h3>Skapa en gratis webbutik</h3>
    <p>Att starta en ebutik med Vendlyx tar inte mer än 5 minuter. Skapa ett konto för att komma igång. Ingenting behöver installeras på din dator.</p>
  </div>
  <div class="abs feature" style="left:174px;top:675px">
    <div class="icon"><svg width="28" height="28" viewBox="0 0 28 28" fill="none" stroke="#fff" stroke-width="1.4"><circle cx="14" cy="14" r="12"/><path d="M8 14l4 4 8-8"/></svg></div>
    <h3>Intuitivt användargränssnitt</h3>
    <p>Det går snabb att lägga till nya produkter. Organisera produkter genom att dra och släppa.</p>
  </div>
  <div class="abs feature" style="left:564px;top:675px">
    <div class="icon"><svg width="24" height="24" viewBox="0 0 24 24" fill="none" stroke="#fff" stroke-width="1.4"><circle cx="10" cy="10" r="7"/><path d="M15 15l6 6"/><path d="M6 10a4 4 0 0 1 4-4"/></svg></div>
    <h3>Sökmotoroptimerad</h3>
    <p>Vendlyx är genomgående skapat med sökmotoroptimering som en fokuspunkt</p>
  </div>
  <div class="abs feature" style="left:174px;top:781px">
    <div class="icon"><svg width="24" height="24" viewBox="0 0 24 24" fill="none" stroke="#fff" stroke-width="1.4"><path d="M4 20l1-5L17 3l4 4L9 19z"/><path d="M15 5l4 4M5 15l4 4"/></svg></div>
    <h3>Designa din webshop</h3>
    <p>Välj bland färdiga utseendemallar eller skapa din egen grafiska profil med ett par klick.</p>
  </div>
  <div class="abs feature" style="left:564px;top:781px">
    <div class="icon"><svg width="26" height="20" viewBox="0 0 26 20" fill="none" stroke="#fff" stroke-width="1.4"><path d="M3 16a10 10 0 1 1 20 0"/><path d="M13 14l-4-6"/><circle cx="13" cy="15" r="1.5"/></svg></div>
    <h3>Smart Dashboard</h3>
    <p>Att starta en ebutik med Vendlyx tar inte mer än 5 minuter. Skapa ett konto för att komma igång. Ingenting behöver installeras på din dator.</p>
  </div>
</section>

<div class="abs rule"></div>

<section>
  <div class="abs card" style="left:141px;top:909px"><div class="num">01</div><div class="body"><small>Small</small><strong>Features</strong><p>Neque porro quisquam est qui dolorem ipsum quia dolor.</p></div></div>
  <div class="abs card" style="left:406px;top:909px"><div class="num">02</div><div class="body"><small>Small</small><strong>Features</strong><p>Neque porro quisquam est qui dolorem ipsum quia dolor.</p></div></div>
  <div class="abs card" style="left:671px;top:909px"><div class="num">03</div><div class="body"><small>Small</small><strong>Features</strong><p>Neque porro quisquam est qui dolorem ipsum quia dolor.</p></div></div>
  <div class="abs card" style="left:141px;top:1030px"><div class="num">04</div><div class="body"><small>Small</small><strong>Features</strong><p>Neque porro quisquam est qui dolorem ipsum quia dolor.</p></div></div>
  <div class="abs card" style="left:406px;top:1030px"><div class="num">05</div><div class="body"><small>Small</small><strong>Features</strong><p>Neque porro quisquam est qui dolorem ipsum quia dolor.</p></div></div>
  <div class="abs card" style="left:671px;top:1030px"><div class="num">06</div><div class="body"><small>Small</small><strong>Features</strong><p>Neque porro quisquam est qui dolorem ipsum quia dolor.</p></div></div>
</section>

<footer>
  <div class="abs foot-left"><i></i><i></i><i></i><i></i></div>
  <div class="abs foot-right">Copyright © 2016, www.vendlyx.example, All Rights Reserved.</div>
</footer>

</body>
</html>
```